New Bicycle shop business card

Hi!
I'm looking for a business card for my new proffesional bike mechanics shop. This shop is only for fixing broken bikes and not selling bikes.
Peferbly a modern and sleek and modern design.
Colors: black, grey, red, white
Information:
Name: Rijwielwerkplaats Vanhoutem
Shop owner: Bart Vanhoutem & Sanne Maertens
Website: www.rijwielwerkplaats-vanhoutem.be
Email: info@rijwielwerkplaats-vanhoutem.be
Phone number: +32471902386
Street adres: Kerkweg 64
9970 Oostmoere
Slogan/shop information: Herstellingen van alle merken.
Logo: see files.
Target Market(s)
People who seek a mechanic to fix or upgrade their bikes.
Contact Information for Business Card
Information:
Website: info@rijwielwerkplaats-vanhoutem.be
9970 Oostmoere
Logo: see files.

```html
<!DOCTYPE html>
<html lang="nl">
<head>
<meta charset="utf-8">
<title>Rijwielwerkplaats Vanhoutem – visitekaartje</title>
<link rel="stylesheet" href="https://fonts.googleapis.com/css2?family=Montserrat:wght@800&family=Roboto:wght@400;500&display=swap">
<style>
  :root {
    --backdrop: #d9d9d9;
    --card: #fbfbfb;
    --ink: #1a1a1a;
    --red: #d42a3c;
    --grey: #9a9ea3;
    --grey-light: #c7cacd;
    --white: #ffffff;
  }
  * { box-sizing: border-box; margin: 0; padding: 0; }
  html, body {
    width: 1200px; height: 852px; overflow: hidden;
    background: var(--backdrop);
    font-family: "Roboto", Arial, sans-serif;
    color: var(--ink);
  }
  .canvas { position: relative; width: 1200px; height: 852px; }

  .card {
    position: absolute;
    width: 540px; height: 310px;
    background: var(--card);
    border-radius: 22px;
    overflow: hidden;
    box-shadow: 0 10px 24px rgba(0,0,0,.18);
  }
  .card--front { left: 90px; top: 90px; }
  .card--back  { left: 570px; top: 452px; }

  .wordmark {
    font-family: "Montserrat", Arial, sans-serif;
    font-weight: 800;
    color: var(--ink);
    letter-spacing: .06em;
    text-transform: uppercase;
    line-height: 1.05;
  }
  .wordmark__mark {
    display: inline-block; width: 14px; height: 14px;
    background: var(--red); border-radius: 50%;
  }

  /* front */
  .front__brand {
    position: absolute; left: 0; right: 0; top: 82px;
    display: flex; flex-direction: column; align-items: center; gap: 14px;
    text-align: center; font-size: 30px;
  }
  .front__slogan {
    position: absolute; left: 0; right: 0; top: 232px;
    display: flex; align-items: center; justify-content: center; gap: 14px;
    font-size: 14px;
  }
  .front__slogan::before, .front__slogan::after {
    content: ""; width: 36px; height: 2px; background: var(--red);
  }
  .front__edge {
    position: absolute; left: 0; right: 0; bottom: 0; height: 8px;
    display: flex;
  }
  .front__edge span:first-child { flex: 0 0 45%; background: var(--red); }
  .front__edge span:last-child { flex: 1; background: var(--grey-light); }

  /* back */
  .back__swoosh { position: absolute; inset: 0; }
  .back__brand {
    position: absolute; left: 28px; top: 30px;
    display: flex; align-items: center; gap: 12px; font-size: 19px;
  }
  .contact {
    position: absolute; left: 30px; top: 130px;
    list-style: none; font-size: 13.5px; line-height: 1;
  }
  .contact li { display: flex; align-items: center; gap: 9px; height: 22px; }
  .contact svg { width: 12px; height: 12px; fill: var(--red); flex: none; }
  .person {
    position: absolute; right: 26px; top: 190px; text-align: right; color: var(--white);
  }
  .person__name {
    font-family: "Roboto", Arial, sans-serif; font-weight: 500;
    font-size: 17px; letter-spacing: .03em; text-transform: uppercase;
  }
  .person__role { font-size: 11px; margin-top: 3px; }
</style>
</head>
<body>
<main class="canvas">

  <section class="card card--front" aria-label="Voorkant">
    <div class="front__brand">
      <span class="wordmark__mark"></span>
      <div class="wordmark">Rijwielwerkplaats<br>Vanhoutem</div>
    </div>
    <p class="front__slogan">Herstellingen van alle merken</p>
    <div class="front__edge"><span></span><span></span></div>
  </section>

  <section class="card card--back" aria-label="Achterkant">
    <svg class="back__swoosh" viewBox="0 0 540 310" preserveAspectRatio="none" aria-hidden="true">
      <path d="M40 304 C170 300 250 278 312 232" fill="none" stroke="var(--grey-light)" stroke-width="12" stroke-linecap="round"/>
      <path d="M540 70 C430 72 380 130 330 200 C280 265 200 300 110 310 L540 310 Z" fill="var(--red)"/>
      <path d="M540 58 C422 60 370 118 318 190 C266 258 180 296 60 304" fill="none" stroke="var(--ink)" stroke-width="4"/>
      <path d="M0 286 C70 298 140 306 210 310 L0 310 Z" fill="var(--red)"/>
    </svg>

    <div class="back__brand">
      <span class="wordmark__mark"></span>
      <div class="wordmark">Rijwielwerkplaats<br>Vanhoutem</div>
    </div>

    <ul class="contact">
      <li><svg viewBox="0 0 24 24"><path d="M6.6 10.8a15.1 15.1 0 0 0 6.6 6.6l2.2-2.2a1 1 0 0 1 1-.25 11.4 11.4 0 0 0 3.6.57 1 1 0 0 1 1 1V20a1 1 0 0 1-1 1A17 17 0 0 1 3 4a1 1 0 0 1 1-1h3.5a1 1 0 0 1 1 1c0 1.25.2 2.45.57 3.57a1 1 0 0 1-.25 1z"/></svg>+32471902386</li>
      <li><svg viewBox="0 0 24 24"><path d="M2 5h20v14H2z"/><path d="M3 6l9 7 9-7" fill="none" stroke="#fff" stroke-width="2"/></svg>www.rijwielwerkplaats-vanhoutem.be</li>
      <li><svg viewBox="0 0 24 24"><circle cx="12" cy="12" r="10"/><path d="M2 12h20M12 2c3 3 3 17 0 20M12 2c-3 3-3 17 0 20" fill="none" stroke="#fff" stroke-width="1.5"/></svg>info@rijwielwerkplaats-vanhoutem.be</li>
      <li>Kerkweg 64 9970 Oostmoere</li>
    </ul>

    <div class="person">
      <p class="person__name">Sanne Maertens</p>
      <p class="person__role">Owner</p>
    </div>
  </section>

</main>
</body>
</html>
```